Property development & Investment company Need a logo & business card design

Our name is KT Estates Australia Pty Ltd
Need logo & business card design

Target Market(s)

People dealing in commercial property

Industry/Entity Type

Business

Contact Information for Business Card

KT Estates Australia
Peter Moss Mobile0419 703 646
Email Peter@birchvale-sample.com.au

Font styles to use
Sans Serif

Requirements
Must have
• company name
• contact details
Nice to have
• KT Estates Bold
• Australia Not Bold
Should not have
• To busy of a look

```html
<!DOCTYPE html>
<html lang="en">
<head>
<meta charset="UTF-8">
<title>KT Estates Australia – Business Card</title>
<link rel="stylesheet" href="https://fonts.googleapis.com/css2?family=Raleway:wght@500;600&family=Lato:ital,wght@0,400;0,700;1,700&display=swap">
<style>
  :root {
    --page-bg: #e6e8ec;
    --card-light: #f4f5f7;
    --card-light-edge: #e3e6ea;
    --navy: #13284a;
    --navy-deep: #0f203d;
    --navy-soft: #2b4670;
    --rule-light: #c9d0da;
    --name-grey: #a9afb7;
    --title-grey: #b9bec6;
    --contact-text: #d3d7dd;
    --icon-bg: #c3c8cf;
    --icon-glyph: #2a3a52;
    --tagline: #24406a;
  }
  * { margin: 0; padding: 0; box-sizing: border-box; }
  html, body { width: 1200px; height: 970px; overflow: hidden; }
  body { background: var(--page-bg); position: relative; }

  .business-card {
    position: absolute;
    left: 100px; top: 189px;
    width: 1000px; height: 592px;
    background: linear-gradient(180deg, var(--card-light) 0%, var(--card-light-edge) 100%);
    box-shadow: 0 10px 30px rgba(20, 35, 60, 0.18);
    overflow: hidden;
  }

  .brand-block {
    position: absolute;
    left: 0; right: 0; top: 112px;
    text-align: center;
  }
  .brand-name {
    font-family: "Raleway", sans-serif;
    font-weight: 600;
    font-size: 48px;
    color: var(--navy);
    letter-spacing: 0.5px;
    line-height: 1;
  }
  .brand-tagline {
    margin-top: 18px;
    display: flex;
    align-items: center;
    justify-content: center;
    gap: 12px;
    font-family: "Raleway", sans-serif;
    font-weight: 500;
    font-size: 20px;
    color: var(--tagline);
  }
  .brand-tagline .dash {
    width: 56px; height: 3px;
    background: var(--navy-deep);
  }

  .divider-rules {
    position: absolute;
    left: 0; right: 0; top: 331px;
  }
  .divider-rules .rule { height: 4px; background: var(--navy); }
  .divider-rules .gap { height: 6px; background: var(--rule-light); }
  .divider-rules .rule.thin { height: 3px; }

  .contact-band {
    position: absolute;
    left: 0; right: 0; top: 352px; bottom: 0;
    background: linear-gradient(100deg, var(--navy-deep) 0%, var(--navy-soft) 35%, var(--navy) 65%, var(--navy-deep) 100%);
  }

  .person {
    position: absolute;
    right: 613px; top: 70px;
    text-align: right;
    font-family: "Lato", sans-serif;
  }
  .person-name {
    font-weight: 700;
    font-size: 29px;
    color: var(--name-grey);
  }
  .person-title {
    margin-top: 12px;
    font-weight: 700;
    font-style: italic;
    font-size: 22px;
    color: var(--title-grey);
  }

  .contact-list {
    position: absolute;
    left: 512px; top: 68px;
    list-style: none;
    font-family: "Lato", sans-serif;
  }
  .contact-item {
    display: flex;
    align-items: center;
    gap: 12px;
    height: 44px;
    margin-bottom: 10px;
    font-size: 27px;
    color: var(--contact-text);
  }
  .contact-icon {
    width: 42px; height: 42px;
    border-radius: 5px;
    background: var(--icon-bg);
    display: flex; align-items: center; justify-content: center;
  }
  .contact-icon svg { width: 28px; height: 28px; }
</style>
</head>
<body>
  <section class="business-card">
    <header class="brand-block">
      <div class="brand-name">KT Estates Australia Pty Ltd</div>
      <div class="brand-tagline">
        <span class="dash"></span>
        <span>Property Development &amp; Investment Company</span>
        <span class="dash"></span>
      </div>
    </header>

    <div class="divider-rules">
      <div class="rule"></div>
      <div class="gap"></div>
      <div class="rule thin"></div>
      <div class="gap"></div>
    </div>

    <div class="contact-band">
      <div class="person">
        <div class="person-name">Daniel Hartwell</div>
        <div class="person-title">Chief Operating Officer</div>
      </div>

      <ul class="contact-list">
        <li class="contact-item">
          <span class="contact-icon">
            <svg viewBox="0 0 28 28" aria-hidden="true">
              <path d="M4 10 Q14 3 24 10 L22 13 L18 12 L17 9 Q14 8 11 9 L10 12 L6 13 Z" fill="var(--icon-glyph)"/>
              <path d="M8 14 L20 14 L23 23 L5 23 Z" fill="var(--icon-glyph)"/>
              <circle cx="14" cy="18.5" r="2.6" fill="var(--icon-bg)"/>
            </svg>
          </span>
          <span class="contact-value">0455 218 907</span>
        </li>
        <li class="contact-item">
          <span class="contact-icon">
            <svg viewBox="0 0 28 28" aria-hidden="true">
              <rect x="4" y="7" width="20" height="14" fill="none" stroke="var(--icon-glyph)" stroke-width="2"/>
              <path d="M4 7 L14 16 L24 7" fill="none" stroke="var(--icon-glyph)" stroke-width="2"/>
            </svg>
          </span>
          <span class="contact-value">Peter@birchvale-sample.com.au</span>
        </li>
      </ul>
    </div>
  </section>
</body>
</html>
```